CV/Resume Design Brochure

I require a brochure design for my partner's CV (curriculum vitae or resume in US).

She is looking for work in the retail fashion sector whilst going to university.

It will be a 4 page brochure. A5 size (148mm x 210mm).

The design needs to be professional, modern and eye catching. In particular the colour scheme needs to stand out.

The contact details for the CV contents will be provided to the winning designer only.

Target Market(s)

The target audience is managers of retail stores, in particular fashion outlets.

Industry/Entity Type

Retail

Font styles to use
Serif

Colors

Designer to choose colors to be used in the design.

Requirements
Must have
• Must be eye catching in terms of design and colour, as the target audience will receive a great deal of CVs/resumes. It must also be professional and simply laid out as most managers will simply glance over it at first.
Should not have
• Complicated, intricate design that makes it look unprofessional. It should not have bland, pale colours.

```html
<!DOCTYPE html>
<html lang="en">
<head>
<meta charset="utf-8">
<title>Clara Whitfield CV</title>
<link rel="stylesheet" href="https://fonts.googleapis.com/css2?family=Cinzel:wght@400&family=PT+Serif:wght@700&family=Roboto:wght@300;400&display=swap">
<style>
:root{
  --yellow:#fcea1f;
  --yellow-dot:#f5d90a;
  --ink:#3a3a3a;
  --heading:#4a5058;
  --body:#505050;
  --tag-text:#8a1f12;
  --panel-line:#dcdcdc;
  --frame:#3c3c3c;
  --soft-blue:#cfdcec;
}
*{box-sizing:border-box;margin:0;padding:0}
html,body{width:1000px;height:1200px;overflow:hidden;background:#fff}
.canvas{position:relative;width:1000px;height:1200px;border:2px solid var(--frame);background:#fff;font-family:"Roboto",Arial,sans-serif;color:var(--body)}
.page{position:absolute;background:#fff;border:2px solid var(--panel-line)}
.cover{left:14px;top:13px;width:414px;height:586px;background:var(--yellow);border:2px solid var(--frame)}
.cover-art{position:absolute;left:50px;top:45px;width:340px;height:240px;border-radius:10px;background:linear-gradient(160deg,#3a3a3a 0%,#555 45%,#e9e6df 70%,#b5332b 100%);opacity:.9}
.cover-name{position:absolute;left:0;right:0;top:322px;text-align:center;font-family:"Cinzel",Georgia,serif;font-weight:400;font-size:40px;line-height:44px;letter-spacing:1px;color:var(--ink)}
.contact{position:absolute;left:238px;top:474px;list-style:none}
.contact li{display:flex;align-items:center;height:22px;font-size:9px;color:var(--ink)}
.contact svg{width:12px;height:12px;margin-right:12px}
.tag{position:absolute;left:0;height:27px;padding-top:5px;background:var(--yellow);clip-path:polygon(0 0,100% 0,86% 50%,100% 100%,0 100%);font-family:"PT Serif",Georgia,serif;font-weight:700;font-size:12px;white-space:nowrap;color:var(--tag-text)}
.job,.school{font-family:"PT Serif",Georgia,serif;font-weight:700;font-size:12.5px;white-space:nowrap;color:var(--heading)}
.text{font-size:10.5px;line-height:17.5px;font-weight:300;color:var(--body)}
.bullets{list-style:none}
.bullets li{position:relative;padding-left:22px;font-size:10.5px;line-height:18px;font-weight:300;color:var(--body)}
.bullets li::before{content:"";position:absolute;left:7px;top:6px;width:4px;height:4px;border-radius:50%;background:var(--yellow-dot)}
.art{position:absolute;border-radius:8px;background:var(--soft-blue)}
.about{left:550px;top:16px;width:414px;height:585px}
.history-p2{left:15px;top:615px;width:411px;height:581px}
.education{left:550px;top:609px;width:414px;height:574px}
</style>
</head>
<body>
<div class="canvas">

  <section class="page cover">
    <div class="cover-art" role="img" aria-label="Illustration of a graduation cap with a rolled diploma tied in a red ribbon"></div>
    <h1 class="cover-name">Clara Whitfield<br>CV</h1>
    <ul class="contact">
      <li><svg viewBox="0 0 12 12"><path d="M6 0.5a3.8 3.8 0 0 0-3.8 3.8C2.2 7.2 6 11.5 6 11.5s3.8-4.3 3.8-7.2A3.8 3.8 0 0 0 6 .5z" fill="var(--ink)"/><circle cx="6" cy="4.3" r="1.4" fill="var(--yellow)"/></svg>xxxxxxxxxxxxxxxxxxx</li>
      <li><svg viewBox="0 0 12 12"><path d="M2.5 1l2 2.2-1 1.3c.7 1.5 1.8 2.6 3.1 3.3l1.3-1 2.2 1.9-1.2 1.8C5.6 10.4 1.6 6.4 1 2.3z" fill="var(--ink)"/></svg>xxxxxx</li>
      <li><svg viewBox="0 0 12 12"><rect x="3.2" y="0.8" width="5.6" height="10.4" rx="1" fill="none" stroke="var(--ink)" stroke-width="1.2"/><line x1="5.2" y1="9.5" x2="6.8" y2="9.5" stroke="var(--ink)"/></svg>xxxxxx</li>
      <li><svg viewBox="0 0 12 12"><rect x="1" y="2.5" width="10" height="7" fill="none" stroke="var(--ink)"/><path d="M1 2.5l5 4 5-4" fill="none" stroke="var(--ink)"/></svg>xxxxxxxxxxxx</li>
    </ul>
  </section>

  <section class="page about">
    <div class="tag" style="top:4px;width:124px;padding-left:30px">About me</div>
    <div class="art" style="left:318px;top:28px;width:84px;height:108px" role="img" aria-label="Illustration of the candidate"></div>
    <p class="text" style="position:absolute;left:10px;top:44px;width:400px">
      I am about to begin a degree course in Visual Merchandising<br>and Promotional Design at Westbrook College in September<br>2014. I am looking to gain more experience in the retail<br>environment to increase my future employment prospects as<br>a visual merchandiser or buyer. Ideally I would be looking for<br>a position that would last three years until the end of my degree,<br>although I am willing to work on a temporary basis. I am available to<br>work 10 – 15 hours per week. Due to my university commitments I am only able to<br>work on a Tuesday, Friday, Saturday or Sunday.<br>My main attributes include team working, friendly personality, willingness<br>to go the extra mile and passion for<br>working in the retail sector.</p>
    <div class="art" style="left:306px;top:272px;width:96px;height:106px;border-radius:50%;opacity:.8" role="img" aria-label="Clock illustration"></div>
    <div class="tag" style="top:299px;width:156px;padding-left:8px">Employment History</div>
    <h2 class="job" style="position:absolute;left:8px;top:336px">Northgate Hospital - Outpatients Clerk - 2008-Present</h2>
    <ul class="bullets" style="position:absolute;left:3px;top:364px;width:405px">
      <li style="margin-bottom:10px">Working confidentially, in accordance with the Data Protection<br>Act, to ensure that patients personal information is not disclosed to<br>outside parties without their permission</li>
      <li style="margin-bottom:12px">Answering calls from patients and relatives regarding their outpatients<br>appointments/referrals</li>
      <li style="margin-bottom:12px">Regular communication with GP’s, Consultants, patients internal and external<br>hospital staff, through the use of telephone, email and letters.</li>
      <li>Part of a team which helps patient appointments be organised and arranged<br>in the best and convenient manner for all parties involved, by liaising with patients,<br>GP’s and consultants.</li>
    </ul>
  </section>

  <section class="page history-p2">
    <ul class="bullets" style="position:absolute;left:3px;top:5px;width:400px">
      <li style="margin-bottom:8px">Open and sort post so that referrals for patients can be processed quickly and<br>accurately</li>
      <li style="margin-bottom:8px">Arrange ambulance transport and interpreters for patients.</li>
      <li style="margin-bottom:8px">Working to government guidelines by ensuring patient appointments are within<br>set time limits</li>
      <li>I was chosen to pilot a new initiative called ECARE (electronic care record) and<br>used this new software system to increase accuracy and productivity in both<br>Nephrology and Thoracic departments.</li>
    </ul>
    <h2 class="job" style="position:absolute;left:22px;top:186px">Dalemart Leigh - Visual Merchandiser/Sales Assistant - 2004-2008</h2>
    <div class="art" style="left:283px;top:206px;width:64px;height:60px;border-radius:50%;opacity:.7" role="img" aria-label="Customer service headset icon"></div>
    <ul class="bullets" style="position:absolute;left:3px;top:232px;width:400px">
      <li style="margin-bottom:8px">Dealing with customer queries to ensure they have<br>a great experience in store</li>
      <li style="margin-bottom:8px">Using an electronic till point and cash handling when serving customers</li>
      <li style="margin-bottom:12px">Replenishing stock on the shop floor and ensuring that the area remained tidy<br>and professionally presented.</li>
      <li style="margin-bottom:12px">Working to guidelines and deadlines to ensure merchandising of Harbour clothing<br>was to high street standard</li>
      <li style="margin-bottom:12px">Meeting deadlines such as relevant pricing, marketing and latest fashion<br>was displayed in accordance with all other stores and in time for national<br>advertisements</li>
      <li style="margin-bottom:12px">Creatively assembling outfits for in store mannequins in order to generate and<br>maximise sales</li>
      <li>Good communication with head office to ensure all of the job were covered,<br>correct advertisements were ordered, and liaising with buyers to clarify were<br>clothing was or any other queries</li>
    </ul>
  </section>

  <section class="page education">
    <div class="tag" style="top:2px;width:110px;padding-left:15px">Education</div>
    <div class="art" style="left:294px;top:19px;width:94px;height:72px;background:linear-gradient(160deg,#5a5a5a,#cfdcec)" role="img" aria-label="Certificate icon"></div>
    <div class="art" style="left:324px;top:132px;width:46px;height:58px;border-radius:23px 23px 6px 6px" role="img" aria-label="Award rosette icon"></div>
    <div class="art" style="left:296px;top:234px;width:82px;height:54px;opacity:.75" role="img" aria-label="Stack of books illustration"></div>
    <h2 class="school" style="position:absolute;left:15px;top:44px">St Aldric’s &nbsp;1999 - 2004</h2>
    <ul class="bullets" style="position:absolute;left:12px;top:66px">
      <li style="line-height:22.5px">GCSE Maths Grade C</li>
      <li style="line-height:22.5px">GCSE English Literature CC</li>
      <li style="line-height:22.5px">GCSE English Language C</li>
      <li style="line-height:22.5px">GCSE Textiles Grade C</li>
      <li style="line-height:22.5px">GCSE French Grade C</li>
      <li style="line-height:22.5px">GCSE P.E. Grade C</li>
    </ul>
    <h2 class="school" style="position:absolute;left:15px;top:225px">Westbrook College</h2>
    <ul class="bullets" style="position:absolute;left:14px;top:257px">
      <li>BA Hons Visual Merchandising and<br>&nbsp;&nbsp;&nbsp;Promotional Design 2014-2017</li>
    </ul>
    <h2 class="school" style="position:absolute;left:15px;top:333px">References available upon request</h2>
  </section>

</div>
</body>
</html>
```